5 post cards for B2B Advertising

We are an electrical lighting contractor advertising our Lighting and Electrical services to property management companies, car dealer ships, hotels, schools, malls, and shopping centers.

RED / White / Blue themed American flag.

Post Cards

1. Electrical Services
2. Lighting Services and conversions to LED
3. Sign Repairs and conversions to LED
4. Nighttime Lighting Inspections (report lights and signs out)
5. Lighting is Safety

```html
<!DOCTYPE html>
<html lang="en">
<head>
<meta charset="utf-8">
<title>Beacon Lamp Works – Postcards</title>
<link rel="stylesheet" href="https://fonts.googleapis.com/css2?family=Oswald:wght@600&family=Poppins:ital,wght@0,400;0,500;0,600;0,800;1,800&display=swap">
<style>
  :root{
    --red:#e31e24;
    --blue:#283593;
    --white:#ffffff;
    --rule:#dcdde2;
    --stamp:#c4c6cc;
    --backdrop:#b3b3b3;
  }
  *{margin:0;padding:0;box-sizing:border-box}
  html,body{width:828px;height:1200px;overflow:hidden}
  body{background:var(--backdrop);font-family:"Poppins",sans-serif}
  .sheet{
    position:absolute;left:12px;top:314px;
    display:grid;grid-template-columns:396px 396px;gap:12px;
  }
  .postcard{width:396px;height:280px;display:block;background:var(--white);box-shadow:0 2px 6px rgba(0,0,0,.35)}
  .brand-name{font-family:"Poppins",sans-serif;font-weight:800;fill:var(--red);text-anchor:middle}
  .headline{font-family:"Poppins",sans-serif;font-weight:800;font-style:italic;font-size:28px}
  .headline-blue{fill:var(--blue)}
  .headline-red{fill:var(--red)}
  .body-copy{font-family:"Poppins",sans-serif;font-weight:500;font-size:11.5px;fill:var(--white);text-anchor:middle}
  .phone-number{font-family:"Oswald",sans-serif;font-weight:600;font-size:40px;fill:var(--white)}
  .contact-line{font-family:"Poppins",sans-serif;font-weight:600;font-size:13.5px;fill:var(--white)}
  .pitch{font-family:"Poppins",sans-serif;font-weight:600;font-size:16px;fill:var(--blue)}
  .pitch-accent{fill:var(--red)}
</style>
</head>
<body>
<main class="sheet">

  <!-- Front: lighting services -->
  <svg class="postcard postcard-front" viewBox="0 0 668 472" aria-label="Postcard front: lighting services and conversions to LED">
    <defs>
      <clipPath id="front-photos-a"><path d="M468,0 L668,0 L668,262 L448,262 C520,170 506,90 468,0 Z"/></clipPath>
      <linearGradient id="sky-a" x1="0" y1="0" x2="0" y2="1"><stop offset="0" stop-color="#c9ccd2"/><stop offset="1" stop-color="#7e858c"/></linearGradient>
      <linearGradient id="field-a" x1="0" y1="0" x2="0" y2="1"><stop offset="0" stop-color="#9fb0a8"/><stop offset="1" stop-color="#3f7a3c"/></linearGradient>
    </defs>
    <rect width="668" height="472" fill="var(--white)"/>
    <g clip-path="url(#front-photos-a)">
      <rect x="440" y="0" width="228" height="155" fill="url(#sky-a)" role="img" aria-label="Photo of a technician in a bucket lift above a white service truck"/>
      <rect x="440" y="160" width="188" height="102" fill="url(#field-a)" role="img" aria-label="Aerial photo of a stadium with field lighting"/>
      <rect x="632" y="160" width="36" height="102" fill="#8b9a8a" role="img" aria-label="Photo of a fleet of service trucks"/>
    </g>
    <path d="M448,0 C490,90 502,170 430,258" fill="none" stroke="var(--red)" stroke-width="9"/>
    <path d="M462,0 C504,90 516,170 446,258" fill="none" stroke="var(--blue)" stroke-width="5"/>
    <path d="M0,238 C220,262 450,264 668,246 L668,346 C450,364 250,372 0,390 Z" fill="var(--blue)"/>
    <path d="M0,398 C250,378 450,370 668,354 L668,472 L0,472 Z" fill="var(--red)"/>

    <text class="brand-name" x="190" y="72" font-size="50">BEACON</text>
    <text class="brand-name" x="190" y="128" font-size="50">LAMP WORKS</text>
    <line x1="45" y1="175" x2="362" y2="175" stroke="var(--rule)" stroke-width="2"/>
    <text class="headline headline-blue" x="48" y="212" textLength="314" lengthAdjust="spacingAndGlyphs">LIGHTING SERVICES &amp;</text>
    <text class="headline headline-red" x="48" y="242" textLength="322" lengthAdjust="spacingAndGlyphs">CONVERSIONS TO LED</text>

    <text class="body-copy" x="334" y="296">Beacon Lamp Works (BLW) provides Night Inspection services for Shopping Centers and Malls!</text>
    <text class="body-copy" x="334" y="311">Free of charge if you sign up for our service agreement.</text>
    <text class="body-copy" x="334" y="339">We'll inspect your property at night documenting any pole, canopy, or security lights that are out.</text>
    <text class="body-copy" x="334" y="354">We also provide photographs of any signs that are in need of repair.</text>

    <circle cx="66" cy="432" r="16" fill="var(--white)"/>
    <path transform="translate(55,421) scale(0.9)" d="M6.6 10.8c1.4 2.8 3.8 5.1 6.6 6.6l2.2-2.2c.3-.3.7-.4 1-.2 1.1.4 2.3.6 3.6.6.6 0 1 .4 1 1V20c0 .6-.4 1-1 1C10.6 21 3 13.4 3 4c0-.6.4-1 1-1h3.5c.6 0 1 .4 1 1 0 1.3.2 2.5.6 3.6.1.3 0 .7-.2 1z" fill="var(--red)"/>
    <text class="phone-number" x="92" y="447" textLength="218" lengthAdjust="spacingAndGlyphs">800-555-0142</text>
    <line x1="338" y1="410" x2="338" y2="454" stroke="var(--white)" stroke-width="2"/>
    <circle cx="366" cy="421" r="6" fill="var(--white)"/>
    <text class="contact-line" x="378" y="426">service@beaconlampworks.com</text>
    <circle cx="366" cy="442" r="6" fill="var(--white)"/>
    <text class="contact-line" x="378" y="447">www.beaconlampworks.com</text>
  </svg>

  <!-- Front: sign repairs -->
  <svg class="postcard postcard-front" viewBox="0 0 668 472" aria-label="Postcard front: sign repairs and conversions to LED">
    <defs>
      <clipPath id="front-photos-b"><path d="M468,0 L668,0 L668,262 L448,262 C520,170 506,90 468,0 Z"/></clipPath>
      <linearGradient id="sky-b" x1="0" y1="0" x2="0" y2="1"><stop offset="0" stop-color="#c9ccd2"/><stop offset="1" stop-color="#7e858c"/></linearGradient>
      <linearGradient id="field-b" x1="0" y1="0" x2="0" y2="1"><stop offset="0" stop-color="#9fb0a8"/><stop offset="1" stop-color="#3f7a3c"/></linearGradient>
    </defs>
    <rect width="668" height="472" fill="var(--white)"/>
    <g clip-path="url(#front-photos-b)">
      <rect x="440" y="0" width="228" height="155" fill="url(#sky-b)" role="img" aria-label="Photo of a technician in a bucket lift above a white service truck"/>
      <rect x="440" y="160" width="188" height="102" fill="url(#field-b)" role="img" aria-label="Aerial photo of a stadium with field lighting"/>
      <rect x="632" y="160" width="36" height="102" fill="#8b9a8a" role="img" aria-label="Photo of a fleet of service trucks"/>
    </g>
    <path d="M448,0 C490,90 502,170 430,258" fill="none" stroke="var(--red)" stroke-width="9"/>
    <path d="M462,0 C504,90 516,170 446,258" fill="none" stroke="var(--blue)" stroke-width="5"/>
    <path d="M0,238 C220,262 450,264 668,246 L668,346 C450,364 250,372 0,390 Z" fill="var(--blue)"/>
    <path d="M0,398 C250,378 450,370 668,354 L668,472 L0,472 Z" fill="var(--red)"/>

    <text class="brand-name" x="190" y="72" font-size="50">BEACON</text>
    <text class="brand-name" x="190" y="128" font-size="50">LAMP WORKS</text>
    <line x1="45" y1="175" x2="362" y2="175" stroke="var(--rule)" stroke-width="2"/>
    <text class="headline headline-blue" x="48" y="212" textLength="268" lengthAdjust="spacingAndGlyphs">SIGN REPAIRS AND</text>
    <text class="headline headline-red" x="48" y="242" textLength="322" lengthAdjust="spacingAndGlyphs">CONVERSIONS TO LED</text>

    <text class="body-copy" x="334" y="296">Beacon Lamp Works (BLW) provides Night Inspection services for Shopping Centers and Malls!</text>
    <text class="body-copy" x="334" y="311">Free of charge if you sign up for our service agreement.</text>
    <text class="body-copy" x="334" y="339">We'll inspect your property at night documenting any pole, canopy, or security lights that are out.</text>
    <text class="body-copy" x="334" y="354">We also provide photographs of any signs that are in need of repair.</text>

    <circle cx="66" cy="432" r="16" fill="var(--white)"/>
    <path transform="translate(55,421) scale(0.9)" d="M6.6 10.8c1.4 2.8 3.8 5.1 6.6 6.6l2.2-2.2c.3-.3.7-.4 1-.2 1.1.4 2.3.6 3.6.6.6 0 1 .4 1 1V20c0 .6-.4 1-1 1C10.6 21 3 13.4 3 4c0-.6.4-1 1-1h3.5c.6 0 1 .4 1 1 0 1.3.2 2.5.6 3.6.1.3 0 .7-.2 1z" fill="var(--red)"/>
    <text class="phone-number" x="92" y="447" textLength="218" lengthAdjust="spacingAndGlyphs">800-555-0142</text>
    <line x1="338" y1="410" x2="338" y2="454" stroke="var(--white)" stroke-width="2"/>
    <circle cx="366" cy="421" r="6" fill="var(--white)"/>
    <text class="contact-line" x="378" y="426">service@beaconlampworks.com</text>
    <circle cx="366" cy="442" r="6" fill="var(--white)"/>
    <text class="contact-line" x="378" y="447">www.beaconlampworks.com</text>
  </svg>

  <!-- Back (two identical mailing sides) -->
  <svg class="postcard postcard-back" viewBox="0 0 668 472" aria-label="Postcard mailing side">
    <defs>
      <clipPath id="back-photos-a"><path d="M0,126 L316,126 C310,200 316,270 332,334 L0,334 Z"/></clipPath>
    </defs>
    <rect width="668" height="472" fill="var(--white)"/>
    <text class="pitch" x="47" y="40">We provide Night Inspection</text>
    <text class="pitch" x="47" y="59">Services and with your</text>
    <text class="pitch" x="47" y="78">approval repair what we find</text>
    <text class="pitch pitch-accent" x="47" y="97">contact us today for a free</text>
    <text class="pitch pitch-accent" x="47" y="116">Lighting Inspection!</text>
    <g clip-path="url(#back-photos-a)">
      <rect x="0" y="126" width="105" height="104" fill="#1f3f6e" role="img" aria-label="Photo of parking lot light fixtures at dusk"/>
      <rect x="0" y="234" width="105" height="100" fill="#4a2f24" role="img" aria-label="Photo of an illuminated storefront sign at night"/>
      <rect x="109" y="126" width="123" height="208" fill="#8f8672" role="img" aria-label="Photo of a technician servicing a pole light"/>
      <rect x="236" y="126" width="100" height="96" fill="#6f8fa8" role="img" aria-label="Photo of a bucket truck raised beside a sign"/>
      <rect x="236" y="226" width="100" height="108" fill="#9aa2a8" role="img" aria-label="Photo of a service van with a technician"/>
    </g>
    <path d="M0,326 C110,312 230,310 326,318 C355,380 385,430 416,472 L0,472 Z" fill="var(--blue)"/>
    <path d="M330,0 C300,130 330,300 420,472" fill="none" stroke="var(--blue)" stroke-width="5"/>
    <path d="M347,0 C317,130 348,300 440,472" fill="none" stroke="var(--red)" stroke-width="10"/>

    <text class="brand-name" x="446" y="46" font-size="24">BEACON</text>
    <text class="brand-name" x="446" y="74" font-size="24">LAMP WORKS</text>
    <rect x="567" y="20" width="73" height="73" fill="var(--stamp)"/>

    <circle cx="66" cy="374" r="17" fill="var(--white)"/>
    <path transform="translate(55,363) scale(0.9)" d="M6.6 10.8c1.4 2.8 3.8 5.1 6.6 6.6l2.2-2.2c.3-.3.7-.4 1-.2 1.1.4 2.3.6 3.6.6.6 0 1 .4 1 1V20c0 .6-.4 1-1 1C10.6 21 3 13.4 3 4c0-.6.4-1 1-1h3.5c.6 0 1 .4 1 1 0 1.3.2 2.5.6 3.6.1.3 0 .7-.2 1z" fill="var(--blue)"/>
    <text class="phone-number" x="95" y="392" font-size="44" textLength="240" lengthAdjust="spacingAndGlyphs">800-555-0142</text>
    <circle cx="56" cy="412" r="6" fill="var(--white)"/>
    <text class="contact-line" x="69" y="417">service@beaconlampworks.com</text>
    <circle cx="56" cy="436" r="6" fill="var(--white)"/>
    <text class="contact-line" x="69" y="441">www.beaconlampworks.com</text>
  </svg>

  <svg class="postcard postcard-back" viewBox="0 0 668 472" aria-label="Postcard mailing side">
    <defs>
      <clipPath id="back-photos-b"><path d="M0,126 L316,126 C310,200 316,270 332,334 L0,334 Z"/></clipPath>
    </defs>
    <rect width="668" height="472" fill="var(--white)"/>
    <text class="pitch" x="47" y="40">We provide Night Inspection</text>
    <text class="pitch" x="47" y="59">Services and with your</text>
    <text class="pitch" x="47" y="78">approval repair what we find</text>
    <text class="pitch pitch-accent" x="47" y="97">contact us today for a free</text>
    <text class="pitch pitch-accent" x="47" y="116">Lighting Inspection!</text>
    <g clip-path="url(#back-photos-b)">
      <rect x="0" y="126" width="105" height="104" fill="#1f3f6e" role="img" aria-label="Photo of parking lot light fixtures at dusk"/>
      <rect x="0" y="234" width="105" height="100" fill="#4a2f24" role="img" aria-label="Photo of an illuminated storefront sign at night"/>
      <rect x="109" y="126" width="123" height="208" fill="#8f8672" role="img" aria-label="Photo of a technician servicing a pole light"/>
      <rect x="236" y="126" width="100" height="96" fill="#6f8fa8" role="img" aria-label="Photo of a bucket truck raised beside a sign"/>
      <rect x="236" y="226" width="100" height="108" fill="#9aa2a8" role="img" aria-label="Photo of a service van with a technician"/>
    </g>
    <path d="M0,326 C110,312 230,310 326,318 C355,380 385,430 416,472 L0,472 Z" fill="var(--blue)"/>
    <path d="M330,0 C300,130 330,300 420,472" fill="none" stroke="var(--blue)" stroke-width="5"/>
    <path d="M347,0 C317,130 348,300 440,472" fill="none" stroke="var(--red)" stroke-width="10"/>

    <text class="brand-name" x="446" y="46" font-size="24">BEACON</text>
    <text class="brand-name" x="446" y="74" font-size="24">LAMP WORKS</text>
    <rect x="567" y="20" width="73" height="73" fill="var(--stamp)"/>

    <circle cx="66" cy="374" r="17" fill="var(--white)"/>
    <path transform="translate(55,363) scale(0.9)" d="M6.6 10.8c1.4 2.8 3.8 5.1 6.6 6.6l2.2-2.2c.3-.3.7-.4 1-.2 1.1.4 2.3.6 3.6.6.6 0 1 .4 1 1V20c0 .6-.4 1-1 1C10.6 21 3 13.4 3 4c0-.6.4-1 1-1h3.5c.6 0 1 .4 1 1 0 1.3.2 2.5.6 3.6.1.3 0 .7-.2 1z" fill="var(--blue)"/>
    <text class="phone-number" x="95" y="392" font-size="44" textLength="240" lengthAdjust="spacingAndGlyphs">800-555-0142</text>
    <circle cx="56" cy="412" r="6" fill="var(--white)"/>
    <text class="contact-line" x="69" y="417">service@beaconlampworks.com</text>
    <circle cx="56" cy="436" r="6" fill="var(--white)"/>
    <text class="contact-line" x="69" y="441">www.beaconlampworks.com</text>
  </svg>

</main>
</body>
</html>
```